K7 Teardown looking for leading edge design not typical for our industry

We need to incorporate our new company tag line "foundations, follow-through, fairness" into our cards. Im open to any type of design for this and colour treatment. In fact the whole card needs a new lay out including the back. "Sustainable Deconstruction" needs to be removed from the back and the new tagline used. Would like to see different text and treatment used for "Deconstruction & Demolition".

Target Market(s)

Construction

Industry/Entity Type

Construction Company

Contact Information for Business Card

Standard business card size

Font styles to use
Sans Serif

Colors
9bcb3c
0255a3
f37122

Requirements
Should not have
• Irregular sizing.

```html
<!DOCTYPE html>
<html lang="en">
<head>
<meta charset="utf-8">
<title>K7 Teardown — Business Card</title>
<link rel="stylesheet" href="https://fonts.googleapis.com/css2?family=Open+Sans:wght@400;700&family=Saira+Semi+Condensed:wght@400;700&family=Saira+Condensed:wght@700&display=swap">
<style>
  :root {
    --teal: #1e6b74;
    --teal-dark: #18555c;
    --green: #8cc04a;
    --orange: #f37122;
    --card: #ffffff;
    --backdrop: #e9e6e1;
    --edge: #d9d9d9;
  }
  * { box-sizing: border-box; margin: 0; padding: 0; }
  html, body { width: 1200px; height: 913px; overflow: hidden; }
  body { background: var(--backdrop); position: relative; font-family: "Open Sans", sans-serif; }

  .card {
    position: absolute;
    width: 540px;
    height: 309px;
    background: var(--card);
    border-radius: 16px;
    box-shadow: 0 2px 0 var(--edge), 0 10px 24px rgba(0,0,0,.12);
  }
  .card--front { left: 50px; top: 110px; }
  .card--back { left: 610px; top: 490px; }

  /* front */
  .brand { position: absolute; left: 30px; top: 120px; display: flex; align-items: center; gap: 12px; }
  .brand__mark { width: 58px; height: 58px; border-radius: 50%; border: 6px solid var(--green); flex: none; }
  .brand__name { font-family: "Saira Semi Condensed", sans-serif; font-weight: 700; font-size: 24px; color: var(--teal); line-height: 1; }
  .descriptor { position: absolute; left: 30px; top: 196px; font-family: "Saira Semi Condensed", sans-serif; color: var(--teal); font-size: 18px; line-height: 1.1; letter-spacing: .3px; }
  .descriptor strong { font-weight: 700; }
  .descriptor small { font-size: 10px; font-weight: 700; }

  .divider { position: absolute; left: 282px; top: 34px; width: 1.5px; height: 240px; background: var(--teal); }

  .contact { position: absolute; left: 298px; top: 34px; color: var(--teal); }
  .contact__name { font-weight: 700; font-size: 22px; line-height: 1.1; }
  .contact__role { color: var(--green); font-size: 13px; margin-bottom: 10px; }
  .contact__address { font-size: 12.5px; line-height: 1.35; margin-bottom: 10px; }
  .contact__list { list-style: none; font-size: 12.5px; line-height: 1.45; }
  .contact__list li { display: flex; align-items: center; gap: 7px; }
  .contact__list svg { width: 10px; height: 10px; flex: none; fill: var(--green); }

  /* back */
  .back-brand { position: absolute; left: 0; right: 0; top: 82px; display: flex; justify-content: center; align-items: center; gap: 18px; }
  .back-brand__mark { width: 78px; height: 78px; border-radius: 50%; border: 9px solid var(--green); }
  .back-brand__name { font-family: "Saira Semi Condensed", sans-serif; font-weight: 700; font-size: 46px; color: var(--teal); line-height: 1; }
  .tagline { position: absolute; left: 0; right: 0; top: 236px; text-align: center; font-family: "Saira Condensed", sans-serif; font-weight: 700; font-size: 22px; text-transform: uppercase; letter-spacing: .5px; }
  .tagline .t1 { color: var(--green); }
  .tagline .t2 { color: var(--orange); }
  .tagline .t3 { color: var(--teal-dark); }
</style>
</head>
<body>

<section class="card card--front" aria-label="Business card front">
  <div class="brand">
    <span class="brand__mark"></span>
    <span class="brand__name">K7 Teardown</span>
  </div>
  <p class="descriptor">DECONSTRUCTION<br><strong>&amp; DEMOLITION</strong> <small>INC</small></p>

  <div class="divider"></div>

  <div class="contact">
    <p class="contact__name">Marcus Hale</p>
    <p class="contact__role">Head Estimator</p>
    <p class="contact__address">#200, 4410 - 87 Street<br>Riverton, AB T4X 1K2</p>
    <ul class="contact__list">
      <li><svg viewBox="0 0 10 10"><path d="M2 0.5l2 2-1 1.2c.6 1.3 1.6 2.3 3 3l1.1-1 2 2-1.3 1.6C4 9 1 6 .5 1.8z"/></svg>(555) 201.4410</li>
      <li><svg viewBox="0 0 10 10"><rect x="2.5" y="0" width="5" height="10" rx="1"/></svg>(555) 377.9021</li>
      <li><svg viewBox="0 0 10 10"><rect x="0.5" y="3" width="9" height="6" rx="1"/><rect x="2.5" y="0.5" width="5" height="3"/></svg>(555) 201.4499</li>
      <li><svg viewBox="0 0 10 10"><path d="M0 2h10v6H0z M0 2l5 3.5L10 2" stroke="#fff" stroke-width=".8"/></svg>marcush@k7teardown.com</li>
      <li><svg viewBox="0 0 10 10"><circle cx="5" cy="5" r="5"/><path d="M0 5h10M5 0v10" stroke="#fff" stroke-width=".8"/></svg>www.k7teardown.com</li>
    </ul>
  </div>
</section>

<section class="card card--back" aria-label="Business card back">
  <div class="back-brand">
    <span class="back-brand__mark"></span>
    <span class="back-brand__name">K7 Teardown</span>
  </div>
  <p class="tagline"><span class="t1">Foundations,</span> <span class="t2">Follow-Through,</span> <span class="t3">Fairness</span></p>
</section>

</body>
</html>
```